Need a small Brochure Designing for a High Tech LED Spotlight

This is an expensive product and the best of it's kind in the world, so it needs to be marketed to intelligent, forward thinking people who appreciate and pay for excellent design and innovation. The type of people who buy Quillon products i guess. It needs to be clean. The colours do not need to be in keep with our website, but our logo does need to be on the brochure. I have attached a dcoument with all the text, the order the text goes in and an idea of how i want the first page to look. All images and logos have been attached too.

Target Market(s)

This is aimed at people with high disposible incomes who spend money on the best designed products and the latest technology. The type of people who buy Quillon products.

Industry/Entity Type

Product

Requirements
Must have
• The work needs to be editable by us using indesign

The pages need to be A5. I'm not sure how many pages the brochure needs to be as it does need to be clean and be spaced out well. On the file that contains the text i've indicated that 8 pages would be good.

The logos i attached - 1) KV Form Merit Prize, 2) Z Engineering Prize, 3) Blue Arc Form Prize and 4) Fine Shape Prize all need to be at the bottom of the front page, quite small, but still able to see them well.

- Needs to have a QR code so that smart phones can scan the code and be taken to a you tube clip - QR code is attached.
- Needs to have Twitter Icon - @BrightThriftLamp
Nice to have
• Nice to remind customers on each page that the product has a 5 year Warranty and we have a 365 day Returns Policy.

```html
<!DOCTYPE html>
<html lang="en">
<head>
<meta charset="utf-8">
<title>K4 LED Spotlight Brochure – Spread Presentation</title>
<link href="https://fonts.googleapis.com/css2?family=Nunito:ital,wght@0,300;0,400;0,700;0,800;1,300&display=swap" rel="stylesheet">
<style>
  :root {
    --green: #3d8b3d;
    --green-soft: #7fae7f;
    --quote-tint: #e2ebe2;
    --ink: #333333;
    --ink-soft: #555555;
    --frame: #9a9a9a;
    --paper: #ffffff;
    --canvas: #ffffff;
    --photo-warm-1: #f3e6d6;
    --photo-warm-2: #e2c8a8;
    --photo-wood: #c89a6a;
    --photo-dark: #3a332c;
  }
  * { box-sizing: border-box; margin: 0; padding: 0; }
  html, body { width: 1200px; height: 900px; overflow: hidden; background: var(--canvas); }
  body { position: relative; font-family: "Nunito", sans-serif; color: var(--ink); }

  .detail-view {
    position: absolute; overflow: hidden; background: var(--paper);
    border: 1px solid var(--frame);
  }
  .detail-view--intro { left: 22px; top: 18px; width: 506px; height: 424px; }
  .detail-view--lifespan { left: 22px; top: 458px; width: 506px; height: 423px; }

  .photo-area {
    position: absolute;
    background: linear-gradient(180deg, var(--photo-warm-1) 0%, #efe0cc 45%, var(--photo-warm-2) 75%, var(--photo-wood) 100%);
  }
  .photo-area--kitchen-dark {
    background: linear-gradient(180deg, #f4ede4 0%, #d9cfc3 40%, var(--photo-dark) 55%, #e9dccb 70%, var(--photo-wood) 100%);
  }
  .text-veil { position: absolute; background: rgba(255,255,255,0.82); }

  .intro-title { position: absolute; left: 93px; top: 164px; font-size: 30px; font-weight: 800; color: var(--green); }
  .intro-lead { position: absolute; left: 93px; top: 222px; width: 760px; font-size: 21px; line-height: 28px; font-weight: 700; letter-spacing: 0.5px; color: var(--ink); white-space: nowrap; }
  .intro-quote { position: absolute; left: 93px; top: 302px; width: 760px; font-size: 21px; line-height: 29px; font-weight: 300; font-style: italic; letter-spacing: 1.6px; color: var(--ink); white-space: nowrap; }
  .intro-quote .source { font-style: normal; letter-spacing: 0.3px; }

  .quote-shape { position: absolute; fill: var(--quote-tint); }
  .detail-view--lifespan .quote-shape { left: 8px; top: 0; width: 250px; height: 190px; }
  .lifespan-pull { position: absolute; left: 281px; top: 106px; width: 700px; font-size: 35px; line-height: 45px; font-weight: 300; font-style: italic; letter-spacing: 1px; color: var(--green-soft); white-space: nowrap; }
  .lifespan-title { position: absolute; left: 61px; top: 326px; font-size: 20px; font-weight: 800; color: var(--green); }
  .lifespan-body { position: absolute; left: 61px; top: 364px; width: 433px; font-size: 14.6px; line-height: 20px; font-weight: 300; text-align: justify; letter-spacing: 0; }

  .connector { position: absolute; left: 0; top: 0; width: 1200px; height: 900px; pointer-events: none; }

  .zoom-badge { position: absolute; width: 37px; height: 37px; border: 1px solid var(--frame); background: var(--paper); }
  .zoom-badge--upper { left: 614px; top: 291px; }
  .zoom-badge--lower { left: 614px; top: 735px; }

  .spread {
    position: absolute; width: 512px; height: 181px; background: var(--paper);
    box-shadow: 0 1px 3px rgba(0,0,0,0.28); overflow: hidden;
  }
  .spread--one { left: 666px; top: 236px; }
  .spread--two { left: 666px; top: 656px; }
  .page { position: absolute; top: 0; width: 256px; height: 181px; overflow: hidden; }
  .page--left { left: 0; }
  .page--right { left: 256px; }

  .mini-col { position: absolute; width: 106px; font-size: 3.6px; line-height: 4.6px; font-weight: 400; color: var(--ink-soft); text-align: justify; }
  .mini-col p { margin-bottom: 2.6px; }
  .mini-col .strong { font-weight: 700; color: var(--ink); }
  .mini-col em { font-style: italic; }
  .mini-head { font-size: 5.2px; line-height: 7px; font-weight: 800; color: var(--green); margin-bottom: 2px; }
  .mini-col .gap { margin-top: 4px; }

  .mini-quote { position: absolute; width: 68px; height: 56px; fill: var(--quote-tint); }
  .mini-pull { position: absolute; font-size: 9.2px; line-height: 12px; font-weight: 300; font-style: italic; color: var(--green-soft); white-space: nowrap; }
</style>
</head>
<body>

  <!-- Enlarged detail: introduction page -->
  <section class="detail-view detail-view--intro">
    <div class="photo-area" style="left:0;top:0;width:506px;height:424px;" role="img" aria-label="Bright modern kitchen interior with framed artwork, colourful tile wall and wooden worktop"></div>
    <div class="text-veil" style="left:43px;top:134px;width:463px;height:290px;"></div>
    <h1 class="intro-title">Introduction</h1>
    <p class="intro-lead">With its unrivalled performance and quality, the K4 7w is the<br>most technologically advanced LED Spotlight in the world.</p>
    <p class="intro-quote">“LEDs used to be prohibitively expensive but advances in<br>semiconductor technology mean they’re brighter and more<br>affordable than before… it’s easy to see why they’re becoming so<br>popular.” <span class="source">Verdict?</span></p>
  </section>

  <!-- Enlarged detail: lifespan page -->
  <section class="detail-view detail-view--lifespan">
    <svg class="quote-shape" viewBox="0 0 250 190" aria-hidden="true">
      <path d="M48 0 H112 L58 186 H8 Z"/>
      <path d="M180 0 H244 L190 186 H140 Z"/>
    </svg>
    <p class="lifespan-pull">You won’t have to replace this<br>LED spotlight for 18 years</p>
    <h2 class="lifespan-title">Lifespan</h2>
    <p class="lifespan-body">As with the brightness testing on the K4, the method used to determine the lamp’s lifespan of this LED Spotlight is also a highly skilled and time consuming exercise known as accelerated testing.</p>
  </section>

  <svg class="connector" viewBox="0 0 1200 900" aria-hidden="true">
    <line x1="528" y1="218" x2="617" y2="292" stroke="#9a9a9a" stroke-width="1"/>
    <line x1="528" y1="655" x2="617" y2="736" stroke="#9a9a9a" stroke-width="1"/>
  </svg>

  <svg class="zoom-badge zoom-badge--upper" viewBox="0 0 37 37" aria-hidden="true">
    <circle cx="16" cy="16" r="8.5" fill="none" stroke="#777" stroke-width="2.4"/>
    <line x1="16" y1="11.5" x2="16" y2="20.5" stroke="#777" stroke-width="2"/>
    <line x1="11.5" y1="16" x2="20.5" y2="16" stroke="#777" stroke-width="2"/>
    <line x1="22.5" y1="22.5" x2="29" y2="29" stroke="#777" stroke-width="3.6" stroke-linecap="round"/>
  </svg>
  <svg class="zoom-badge zoom-badge--lower" viewBox="0 0 37 37" aria-hidden="true">
    <circle cx="16" cy="16" r="8.5" fill="none" stroke="#777" stroke-width="2.4"/>
    <line x1="16" y1="11.5" x2="16" y2="20.5" stroke="#777" stroke-width="2"/>
    <line x1="11.5" y1="16" x2="20.5" y2="16" stroke="#777" stroke-width="2"/>
    <line x1="22.5" y1="22.5" x2="29" y2="29" stroke="#777" stroke-width="3.6" stroke-linecap="round"/>
  </svg>

  <!-- Spread: introduction / heat & brightness -->
  <article class="spread spread--one">
    <div class="page page--left">
      <div class="photo-area photo-area--kitchen-dark" style="left:0;top:0;width:256px;height:181px;" role="img" aria-label="White kitchen with black pendant lamps, colourful tile wall and wooden floor"></div>
      <div class="text-veil" style="left:4px;top:82px;width:252px;height:99px;"></div>
      <div class="mini-col" style="left:14px;top:87px;">
        <div class="mini-head">Introduction</div>
        <p class="strong">With its unrivalled performance and quality, the K4 7w is the most technologically advanced LED Spotlight in the world.</p>
        <p>“LEDs used to be prohibitively expensive but advances in semiconductor technology mean they’re brighter and more affordable than before… it’s easy to see why they’re becoming so popular.” Verdict?</p>
        <p>BrightThriftLamp’s Managing Director Owen Hale talks about the K4 7w LED Spot:</p>
        <p><em>“I’ve been working with the manufacturer of this exceptional product since their inception in 2009. They’ve received more than a hundred world awards and safety certifications so far – as far as I am concerned, there isn’t an LED manufacturer in the</em></p>
      </div>
      <div class="mini-col" style="left:131px;top:94px;">
        <p><em>world that comes close to their expertise and attention to detail.</em></p>
        <p><em>Since its creation, the company has won a number of prestigious international design awards, such as Germany’s KV Form Merit Prize, the Z Engineering Prize, the Blue Arc Form Prize and Japan’s Fine Shape Prize.</em></p>
        <p><em>With high-quality, industry-leading performance, they’ve become the first choice for professional buyers and lighting designers in recent years. They’re basically the Quillon of the LED lighting industry – we’re selling beautifully designed products that are miles ahead of the competition.</em></p>
        <p><em>The K4 7w: The Ultimate In Lighting For The Discerning, Design Conscious And Forward Thinking Person!</em></p>
      </div>
    </div>
    <div class="page page--right">
      <svg class="mini-quote" style="left:0;top:2px;" viewBox="0 0 250 190" aria-hidden="true">
        <path d="M48 0 H112 L58 186 H8 Z"/>
        <path d="M180 0 H244 L190 186 H140 Z"/>
      </svg>
      <p class="mini-pull" style="left:71px;top:30px;">Cut your energy consumption<br>by up to 90%”</p>
      <div class="mini-col" style="left:16px;top:87px;">
        <div class="mini-head">Heat Dissipation</div>
        <p>The brightness of all LEDs deteriorates over time. Just how quickly, though, is almost exclusively down to how well the lamp can dissipate heat.</p>
        <p>Heat is the biggest enemy of the LED. Without proper heat dissipation, the critical components of any LED lamp will fail or degrade quickly. The K4 has a well-designed, thorough heat dissipation system, so light output stays steady for years.</p>
        <p>The K4 body is crafted from the finest raw materials and uses a cutting edge heat dissipation system so that it remains cool to the touch.</p>
        <p>This beautiful, intuitive, patented design has won multiple international awards.</p>
      </div>
      <div class="mini-col" style="left:131px;top:87px;">
        <div class="mini-head">Brightness</div>
        <p>Lumora manufactures the most advanced and powerful LED chips in the world. While most producers now offer cheaper alternatives, there is still no substitute for quality.</p>
        <p>The K4 uses the very latest Lumora LX-9 Chip, which produces 580 warm white lumens. With 83 lumens per watt, the K4 is considerably more powerful than a 50w halogen.</p>
        <p>An integrating sphere is used to measure the total light radiated in all directions from the lamp, giving customers a 100% accurate measurement of its true power.</p>
      </div>
    </div>
  </article>

  <!-- Spread: lifespan & dimensions / warranty & colour -->
  <article class="spread spread--two">
    <div class="page page--left">
      <svg class="mini-quote" style="left:2px;top:0;" viewBox="0 0 250 190" aria-hidden="true">
        <path d="M48 0 H112 L58 186 H8 Z"/>
        <path d="M180 0 H244 L190 186 H140 Z"/>
      </svg>
      <p class="mini-pull" style="left:72px;top:30px;">You won’t have to replace this<br>LED spotlight for 18 years</p>
      <div class="mini-col" style="left:16px;top:86px;">
        <div class="mini-head">Lifespan</div>
        <p>As with the brightness testing on the K4, the method used to determine the lamp’s lifespan of this LED Spotlight is also a highly skilled and time consuming exercise known as accelerated testing.</p>
        <p>We use an algorithm that, after around 6,000 hours of testing, calculates the number of hours remaining before the LED’s light will start to lose a significant amount of its brightness. Tests take up to 12 months to complete, ensuring that customers get a product with real staying power.</p>
        <div class="mini-head gap">Easy Installation</div>
        <p>The K4 comes in two standard fittings, GU10 (twist and lock) and MR16 (two pin). Installation is simple: just take your old halogens out and put the K4 in.</p>
      </div>
      <div class="mini-col" style="left:131px;top:86px;">
        <div class="mini-head">Product Dimensions</div>
        <p>GU10 – Length 60mm x Width 50mm<br>MR16 – Length 48.5mm x Width 50mm</p>
        <p>Please note: the dimmable K4 only comes in GU10 fitting.</p>
        <div class="mini-head gap">Beam Angle</div>
        <p>The K4 is available in two different beam angles, 60 and 135 degrees.</p>
        <p>The wide beam angle of 135 degrees means this product is perfect for any well-lit living room. However, if you have smaller areas to light, the 60 degree beam is ideal for accent and task lighting – ask our expert team and we’ll help you make the best decision for your property.</p>
      </div>
    </div>
    <div class="page page--right">
      <div class="photo-area photo-area--kitchen-dark" style="left:0;top:0;width:256px;height:181px;" role="img" aria-label="Open plan kitchen and living space with large windows and light wooden floor"></div>
      <div class="text-veil" style="left:0;top:82px;width:252px;height:99px;"></div>
      <div class="mini-col" style="left:16px;top:86px;">
        <div class="mini-head">Warranty &amp; Returns</div>
        <p>We’re sure the K4 is the best LED Spotlight in the world, which is why we’ve given it the best warranty and returns period in the world.</p>
        <p>This product comes with an industry-leading five year comprehensive warranty and a 365-day returns period, offering you complete security and satisfaction.</p>
        <div class="mini-head gap">Maintenance</div>
        <p>With an expected lifespan of 40,000 hours the K4 will last for an average of over 18 years if used for six hours a day, 365 days a year. With a lifespan like this, savings on replacing failed lamps are enormous.</p>
      </div>
      <div class="mini-col" style="left:131px;top:86px;">
        <div class="mini-head">Colour Temperature</div>
        <p>The K4 comes in two different colour temperatures:</p>
        <p>Warm White – The colour we highly recommend for your home. Not quite as warm as a halogen but still carries the warm glow with a cleaner light quality.</p>
        <p>Natural White – Perfect for commercial properties such as retail stores. Very clean and bright colour temperature, which will illuminate the room to its optimum.</p>
      </div>
    </div>
  </article>

</body>
</html>
```